CD Cover for Professional Metaphysical Album

I actually have two Meditation albums ready to go out digitally. Needs somewhat consistent appearance for both as they are from same author - however audio themes are very different. Prior attempts with 5 other designers elsewhere failed to turn up professional level results. Im happy to discuss producing immediately a 2nd album as I see CD 1 succeeding.

CD 1 Title needs to read Quiet River Reflections
My name needs to appear at bottom I presume .. Marcus Doyle
*I am fairly certain of how I'd like cover to appear - white horizontal rectangular area above/below image where text is inserted. I have some examples attached to consider/inspire you. Willing to go outside the box in thinking.

CD 1 (image: AmberTide Horizon-Selvaroth-300DPI) is the MASTER IMAGE to work from.

This project we already know will be purchased mostly by women, if such matters.

Target Market(s)

metaphysical, spiritual, meditation, metaphysics

Industry/Entity Type

Religious

Colors

Designer to choose colors to be used in the design.

Requirements
Must have
• Title : Quiet River Reflections
• Author name: Marcus Doyle
• White header footer preferred strongly but will consider options
• Eye catching fonts but im poor with picking such! Need your expertise on font color also!
Nice to have
• unsure
Should not have
• unsure

```html
<!DOCTYPE html>
<html lang="en">
<head>
<meta charset="utf-8">
<title>Quiet River Reflections — Marcus Doyle</title>
<link rel="stylesheet" href="https://fonts.googleapis.com/css2?family=EB+Garamond:wght@400;500&display=swap">
<style>
  :root {
    --backdrop: #e4e4e4;
    --cover-white: #ffffff;
    --ink: #111111;
    --ornament-mid: #e6e6ee;
    --ornament-edge: #f6f6f9;
    --ring-blue: #2f9fd8;
    --ring-cyan: #6fd6f2;
    --ring-deep: #1d5fa8;
    --core-violet: #8a3fc0;
    --core-magenta: #d2358f;
    --core-amber: #f3a23a;
    --core-glow: #fff1c8;
  }
  html, body {
    margin: 0;
    padding: 0;
    width: 1200px;
    height: 800px;
    overflow: hidden;
    background: var(--backdrop);
  }
  .canvas {
    position: relative;
    width: 1200px;
    height: 800px;
  }
  .album-cover {
    position: absolute;
    left: 240px;
    top: 40px;
    width: 720px;
    height: 720px;
    background: var(--cover-white);
    font-family: "EB Garamond", Garamond, serif;
    color: var(--ink);
    text-align: center;
    overflow: hidden;
  }
  .floral-field,
  .master-artwork {
    position: absolute;
    left: 0;
    top: 0;
    width: 720px;
    height: 720px;
  }
  .album-title {
    position: absolute;
    left: 0;
    right: 0;
    top: 6px;
    margin: 0;
    font-weight: 400;
    line-height: 1;
  }
  .album-title__lead {
    display: block;
    font-size: 74px;
    letter-spacing: 1px;
    margin-left: -20px;
  }
  .album-title__rest {
    display: block;
    font-size: 47px;
    margin-top: 4px;
    margin-left: 60px;
  }
  .artist-name {
    position: absolute;
    left: 0;
    right: 0;
    top: 648px;
    margin: 0;
    font-size: 41px;
    font-weight: 400;
    line-height: 1;
  }
</style>
</head>
<body>
<div class="canvas">
  <section class="album-cover">
    <svg class="floral-field" viewBox="0 0 720 720" role="img" aria-label="Fine grey floral line work radiating around the central artwork like a mandala of lilies and buds">
      <defs>
        <radialGradient id="floral-tone" cx="50%" cy="50%" r="50%">
          <stop offset="0%" stop-color="var(--ornament-mid)"/>
          <stop offset="70%" stop-color="var(--ornament-edge)"/>
          <stop offset="100%" stop-color="#ffffff" stop-opacity="0"/>
        </radialGradient>
      </defs>
      <ellipse cx="362" cy="408" rx="352" ry="330" fill="url(#floral-tone)"/>
    </svg>

    <svg class="master-artwork" viewBox="0 0 720 720" role="img" aria-label="Master image AmberTide Horizon: a glowing violet, magenta and amber circle with a seated meditating silhouette, edged by a painted blue brush ring">
      <defs>
        <radialGradient id="brush-ring" cx="50%" cy="50%" r="50%">
          <stop offset="78%" stop-color="var(--ring-cyan)"/>
          <stop offset="92%" stop-color="var(--ring-blue)"/>
          <stop offset="100%" stop-color="var(--ring-deep)"/>
        </radialGradient>
        <radialGradient id="meditation-core" cx="50%" cy="55%" r="55%">
          <stop offset="0%" stop-color="var(--core-glow)"/>
          <stop offset="18%" stop-color="var(--core-amber)"/>
          <stop offset="45%" stop-color="var(--core-magenta)"/>
          <stop offset="80%" stop-color="var(--core-violet)"/>
          <stop offset="100%" stop-color="#5b3aa8"/>
        </radialGradient>
      </defs>
      <circle cx="364" cy="404" r="252" fill="url(#brush-ring)"/>
      <circle cx="364" cy="404" r="208" fill="url(#meditation-core)"/>
    </svg>

    <h1 class="album-title">
      <span class="album-title__lead">QUIET</span>
      <span class="album-title__rest">River Reflections</span>
    </h1>
    <p class="artist-name">Marcus Doyle</p>
  </section>
</div>
</body>
</html>
```